Brightwave Travel and Tours

Hotel Reservations
Airline Ticketing
Day Tour

My business is a Travel agency. My services are issuing domestic and international tickets. Book room/hotel reservations local/international.
My color preference is apple green/orange/red/blue.
Images of beaches, tickets,luggage.

```html
<!DOCTYPE html>
<html lang="en">
<head>
<meta charset="utf-8">
<title>Brightwave Travel and Tours – Business Card</title>
<link rel="stylesheet" href="https://fonts.googleapis.com/css2?family=Signika:wght@600&family=Roboto+Condensed:wght@400&family=Roboto:wght@400&display=swap">
<style>
  :root {
    --stage: #000000;
    --sky-top: #74c9ef;
    --sky-mid: #bfe6f7;
    --haze: #f4f9fb;
    --sea-dark: #2a8fa8;
    --sea-light: #5cc6cf;
    --foam: #e9f4f5;
    --sand: #e7e4df;
    --brand: #1d6f93;
    --name: #0e5a93;
    --ink: #1e1e1e;
    --muted: #6b6b6b;
    --accent-blue: #0f74bb;
    --tag-blue: #0f74bb;
    --tag-green: #2bb04a;
    --tag-orange: #f7941d;
    --white: #ffffff;
  }
  * { box-sizing: border-box; margin: 0; padding: 0; }
  html, body { width: 1200px; height: 1000px; overflow: hidden; background: var(--stage); }
  .canvas { position: relative; width: 1200px; height: 1000px; }

  .card {
    position: absolute; left: 269px; width: 662px; height: 368px; overflow: hidden;
  }
  .card--front { top: 128px; }
  .card--back { top: 504px; }

  .beach-scene {
    position: absolute; inset: 0;
    background: linear-gradient(to bottom,
      var(--sky-top) 0%, var(--sky-mid) 38%, var(--haze) 70%,
      #d9dde0 74%, var(--sea-dark) 77%, var(--sea-light) 81%,
      var(--foam) 86%, var(--sand) 90%, var(--sand) 100%);
  }

  .brand-mark { position: absolute; display: flex; flex-direction: column; align-items: center; }
  .brand-mark__dot { border-radius: 50%; background: var(--brand); }
  .brand-mark__name {
    font-family: "Signika", sans-serif; font-weight: 600; color: var(--brand);
    text-align: center; line-height: 1.05; text-transform: uppercase;
  }
  .card--front .brand-mark { left: 30px; top: 40px; width: 130px; }
  .card--front .brand-mark__dot { width: 46px; height: 46px; margin-bottom: 8px; }
  .card--front .brand-mark__name { font-size: 13px; }

  .company-title {
    position: absolute; left: 190px; top: 50px;
    font-family: "Signika", sans-serif; font-weight: 600; font-size: 25px;
    color: var(--brand); text-transform: uppercase; letter-spacing: 0.2px; white-space: nowrap;
  }
  .services { position: absolute; left: 190px; top: 84px; display: flex; gap: 4px; }
  .services__tag {
    height: 23px; line-height: 23px; padding: 0 14px;
    font-family: "Roboto Condensed", sans-serif; font-size: 17px; color: var(--white);
  }
  .services__tag--hotel { background: var(--tag-blue); width: 163px; }
  .services__tag--air { background: var(--tag-green); width: 146px; }
  .services__tag--day { background: var(--tag-orange); width: 97px; }

  .offer { position: absolute; left: 193px; top: 114px; font-family: "Roboto", sans-serif; font-size: 14px; line-height: 19px; color: var(--ink); }

  .travel-gear {
    position: absolute; left: 36px; top: 162px; width: 180px; height: 186px;
    background: linear-gradient(120deg, #2b2d31 0%, #2b2d31 45%, #eef0f0 46%, #d9dcdc 100%);
    border-radius: 8px;
  }

  .holder-name {
    position: absolute; left: 210px; top: 188px;
    font-family: "Roboto Condensed", sans-serif; font-size: 29px; color: var(--name);
  }
  .contact { position: absolute; left: 393px; top: 173px; font-family: "Roboto Condensed", sans-serif; font-size: 19px; line-height: 25px; color: var(--muted); }
  .contact__label { color: var(--accent-blue); font-weight: 700; margin-right: 4px; }

  .card--back .brand-mark { left: 0; right: 0; top: 70px; }
  .card--back .brand-mark__dot { width: 90px; height: 90px; margin-bottom: 22px; }
  .card--back .brand-mark__name { font-size: 32px; }
</style>
</head>
<body>
<main class="canvas">
  <section class="card card--front">
    <div class="beach-scene" role="img" aria-label="Photo of a tropical beach with blue sky, turquoise sea and white sand"></div>
    <div class="brand-mark">
      <span class="brand-mark__dot"></span>
      <span class="brand-mark__name">Brightwave<br>Travel and Tours</span>
    </div>
    <h1 class="company-title">Brightwave Travel and Tours</h1>
    <ul class="services" style="list-style:none">
      <li class="services__tag services__tag--hotel">Hotel Reservations</li>
      <li class="services__tag services__tag--air">Airline Ticketing</li>
      <li class="services__tag services__tag--day">Day Tour</li>
    </ul>
    <p class="offer">Domestic and International Tickets.<br>Book Room/Hotel Reservations Local/International.</p>
    <div class="travel-gear" role="img" aria-label="Photo of a black rolling suitcase with boarding pass tickets"></div>
    <p class="holder-name">Name Name</p>
    <address class="contact" style="font-style:normal">
      Address Line 1, Line 2,<br>
      <span class="contact__label">P</span>055 555 555<br>
      <span class="contact__label">E</span>contact@brightwavetravel.com
    </address>
  </section>

  <section class="card card--back">
    <div class="beach-scene" role="img" aria-label="Photo of a tropical beach with blue sky, turquoise sea and white sand"></div>
    <div class="brand-mark">
      <span class="brand-mark__dot"></span>
      <span class="brand-mark__name">Brightwave<br>Travel and Tours</span>
    </div>
  </section>
</main>
</body>
</html>
```